PowerPoint Template - Multiple Slide Backgrounds

Looking for a professional PowerPoint template for a technology company. You will see with the logo there's sort of a theme with gears and a lightbulb of sorts. Keeping with this sort of design could help with the brand.

Branding information
• Logo with transparent background included
• Primary Color (Orange) Hex #E6753D
• Secondary Color (Brown) Hex #6A4238
• Primary Font - Myriad Pro
• Secondary Font - Quiet Sans Light

Design request -
• PowerPoint (POTX) template with master slide views
• Cover Slide
• Color Pallet - 7 Color PowerPoint pallet that includes and complements primary and secondary colors
• Slide Master with Footer
• Multiple Background Types to allow for smart art overlay or bullet point text boxes
Bonus - Sample graphical elements using shapes and smart art

```html
<!DOCTYPE html>
<html lang="en">
<head>
<meta charset="utf-8">
<title>Ridgeway DevOps – Presentation Template</title>
<link href="https://fonts.googleapis.com/css2?family=Source+Sans+3:wght@400;600;700;800&display=swap" rel="stylesheet">
<style>
:root{
  --orange:#E6753D;
  --brown:#6A4238;
  --rust:#8A3C26;
  --copper:#B8562A;
  --ink:#111111;
  --text:#3a3a3a;
  --paper:#ffffff;
  --stage:#f1f1f1;
  --board:#58595b;
  --arrow:#c9c9c9;
}
*{box-sizing:border-box;margin:0;padding:0}
html,body{width:1200px;height:2647px;overflow:hidden}
body{position:relative;background:var(--board);font-family:"Source Sans 3",Arial,sans-serif;color:var(--text)}

.hero{position:absolute;left:0;top:0;width:1200px;height:803px;background:var(--stage)}
.hero .slide{left:250px;top:200px;transform:scale(1.294);transform-origin:0 0}

.slide{position:absolute;width:541px;height:303px;background:var(--paper);overflow:hidden;box-shadow:0 6px 14px rgba(0,0,0,.35)}
.slide svg.art{position:absolute;left:0;top:0}

/* shared slide chrome */
.top-rule{position:absolute;top:19px;left:150px;right:0;height:1px;background:var(--brown)}
.top-rule::before{content:"";position:absolute;left:0;top:-1px;width:40px;height:3px;background:var(--orange)}
.brand-mini{position:absolute;top:5px;right:10px;font-size:9px;font-weight:700;color:var(--brown)}
.foot-url{position:absolute;left:10px;bottom:11px;font-size:7px;font-weight:600;letter-spacing:.5px;color:var(--brown)}
.foot-rule{position:absolute;left:0;right:24px;bottom:6px;height:2px;background:var(--orange)}
.page-no{position:absolute;right:6px;bottom:2px;width:14px;height:14px;border-radius:50%;background:var(--brown);color:#fff;font-size:6px;font-weight:700;display:flex;align-items:center;justify-content:center}
.heading{position:absolute;left:10px;top:26px;font-size:11px;font-weight:800;color:var(--brown)}
.heading::after{content:"";display:block;margin-top:3px;width:100%;height:2px;background:linear-gradient(90deg,var(--orange) 30%,var(--brown) 30%)}
.photo{position:absolute}

/* cover */
.cover-brand{position:absolute;left:30px;top:62px;display:flex;align-items:center;gap:8px;font-size:20px;font-weight:800;color:var(--brown)}
.dot{display:inline-block;width:16px;height:16px;border-radius:50%;background:var(--orange)}
.cover-kicker{position:absolute;left:0;top:152px;width:232px;height:20px;background:var(--brown);color:#fff;font-size:13px;padding-left:10px;line-height:20px}
.cover-title{position:absolute;left:10px;top:172px;font-size:36px;font-weight:800;color:var(--ink);line-height:1;letter-spacing:-.5px}
.cover-sub{position:absolute;left:10px;top:210px;font-size:25px;font-weight:700;color:var(--orange);line-height:1;letter-spacing:-.3px}
.cover-foot{position:absolute;left:0;bottom:8px;width:180px;height:14px;background:var(--orange);color:#fff;font-size:8px;font-weight:700;letter-spacing:.8px;padding-left:22px;line-height:14px}
.cover-foot::before{content:"";position:absolute;left:8px;top:3px;width:8px;height:8px;border-radius:50%;border:1.5px solid #fff}
.cover-line{position:absolute;left:0;right:180px;bottom:4px;height:1px;background:var(--orange)}

/* contents */
.toc{position:absolute;left:318px;top:84px;width:198px}
.toc h2{font-size:12px;font-weight:800;color:var(--brown);padding-bottom:4px;border-bottom:2px solid var(--orange);width:140px;margin-bottom:12px}
.toc li{list-style:none;display:flex;justify-content:space-between;font-size:7.5px;color:var(--ink);height:21px}

/* info boxes */
.info-box{position:absolute;top:100px;height:168px;background:var(--brown);color:#fff;padding:10px 9px}
.info-box h3{font-size:9px;font-weight:700;text-align:center;margin-bottom:6px}
.info-box p{font-size:6.5px;line-height:1.35;margin-bottom:6px}

/* title slide */
.center-brand{position:absolute;left:0;right:0;top:110px;display:flex;justify-content:center;align-items:center;gap:10px;font-size:26px;font-weight:800;color:var(--brown)}
.center-title{position:absolute;left:0;right:0;top:204px;text-align:center;font-size:18px;font-weight:800;color:var(--orange)}

/* ring slide */
.ring-label{position:absolute;left:10px;top:150px}
.ring-label h3{font-size:17px;font-weight:800;color:var(--brown);line-height:1}
.ring-label p{font-size:8px;color:var(--orange)}
.point{position:absolute;left:396px;width:140px;font-size:7px;line-height:1.3;color:var(--ink)}

/* grid slide */
.cell{position:absolute;width:160px;padding-left:30px}
.cell b{display:block;font-size:9.5px;font-weight:700;color:var(--brown)}
.cell b.hot{color:var(--orange)}
.cell span{display:block;font-size:6.3px;line-height:1.25;color:var(--ink)}
.cell i{position:absolute;left:0;top:0;width:22px;height:22px;border-radius:50%;color:#fff;font-style:normal;font-size:8px;font-weight:700;display:flex;align-items:center;justify-content:center}

/* percent slides */
.note{position:absolute;width:112px;font-size:7px;line-height:1.3;text-align:center;color:var(--ink)}

/* closing */
.closing{background:var(--brown);color:#fff}
.closing-brand{position:absolute;left:0;width:250px;top:136px;display:flex;flex-direction:column;align-items:center;gap:10px;font-size:24px;font-weight:800}
.closing-brand .dot{width:20px;height:20px;background:#fff}
.thanks{position:absolute;left:318px;top:44px;font-size:28px;font-weight:800}
.contact{position:absolute;padding-left:22px;font-size:8px;font-weight:600}
.contact small{display:block;font-size:6px;font-weight:400;opacity:.9}
.contact svg{position:absolute;left:0;top:0}

.signoff{position:absolute;left:632px;top:2280px;width:541px;height:303px;display:flex;flex-direction:column;align-items:center;justify-content:center;gap:12px;color:#fff;font-size:34px;font-weight:800}
.signoff .dot{width:26px;height:26px;background:#fff}
</style>
</head>
<body>

<section class="hero">
  <div class="slide cover">
    <svg class="art" width="541" height="303" viewBox="0 0 541 303">
      <defs><linearGradient id="heroPhoto" x1="0" y1="0" x2="1" y2="1"><stop offset="0" stop-color="#5f7f52"/><stop offset=".55" stop-color="#c9a79c"/><stop offset="1" stop-color="#e9ddd6"/></linearGradient></defs>
      <circle cx="470" cy="80" r="128" fill="url(#heroPhoto)" role="img" aria-label="Photo of a smiling professional on the phone"/>
      <path d="M306 -35 A200 200 0 0 0 297 180" fill="none" stroke="var(--ink)" stroke-width="10"/>
      <path d="M308 21 A172 172 0 0 0 556 229" fill="none" stroke="var(--orange)" stroke-width="30"/>
      <path d="M327 55 A145 145 0 0 0 520 216" fill="none" stroke="var(--brown)" stroke-width="22"/>
      <path d="M284 187 A215 215 0 0 0 507 292" fill="none" stroke="var(--brown)" stroke-width="1.5"/>
      <circle cx="284" cy="187" r="3" fill="var(--orange)"/><circle cx="507" cy="292" r="3" fill="var(--ink)"/>
      <path d="M295 -20 A230 230 0 0 0 262 110" fill="none" stroke="var(--orange)" stroke-width="1.5"/>
      <circle cx="262" cy="110" r="3" fill="var(--orange)"/>
    </svg>
    <div class="cover-brand"><span class="dot"></span>Ridgeway DevOps</div>
    <div class="cover-kicker">LOREM IPSUM IS SIMPLY DUMMY</div>
    <div class="cover-title">LOREM TEXT</div>
    <div class="cover-sub">LOREM IPSUM TEXT</div>
    <div class="cover-line"></div>
    <div class="cover-foot">www.webaddress.com</div>
  </div>
</section>

<!-- row 1 -->
<div class="slide cover" style="left:49px;top:863px">
  <svg class="art" width="541" height="303" viewBox="0 0 541 303">
    <defs><linearGradient id="coverPhoto" x1="0" y1="0" x2="1" y2="1"><stop offset="0" stop-color="#5f7f52"/><stop offset=".55" stop-color="#c9a79c"/><stop offset="1" stop-color="#e9ddd6"/></linearGradient></defs>
    <circle cx="470" cy="80" r="128" fill="url(#coverPhoto)" role="img" aria-label="Photo of a smiling professional on the phone"/>
    <path d="M306 -35 A200 200 0 0 0 297 180" fill="none" stroke="var(--ink)" stroke-width="10"/>
    <path d="M308 21 A172 172 0 0 0 556 229" fill="none" stroke="var(--orange)" stroke-width="30"/>
    <path d="M327 55 A145 145 0 0 0 520 216" fill="none" stroke="var(--brown)" stroke-width="22"/>
    <path d="M284 187 A215 215 0 0 0 507 292" fill="none" stroke="var(--brown)" stroke-width="1.5"/>
    <circle cx="284" cy="187" r="3" fill="var(--orange)"/><circle cx="507" cy="292" r="3" fill="var(--ink)"/>
    <path d="M295 -20 A230 230 0 0 0 262 110" fill="none" stroke="var(--orange)" stroke-width="1.5"/>
    <circle cx="262" cy="110" r="3" fill="var(--orange)"/>
  </svg>
  <div class="cover-brand"><span class="dot"></span>Ridgeway DevOps</div>
  <div class="cover-kicker">LOREM IPSUM IS SIMPLY DUMMY</div>
  <div class="cover-title">LOREM TEXT</div>
  <div class="cover-sub">LOREM IPSUM TEXT</div>
  <div class="cover-line"></div>
  <div class="cover-foot">www.webaddress.com</div>
</div>

<div class="slide contents" style="left:632px;top:863px">
  <div class="photo" role="img" aria-label="Photo of hands typing on a laptop at a wooden desk" style="left:0;top:0;width:278px;height:270px;background:linear-gradient(135deg,#9a6a4a,#d9c3b0 55%,#f2ece6)"></div>
  <div class="top-rule" style="left:290px"></div><span class="brand-mini">Ridgeway DevOps</span>
  <div class="toc">
    <h2>TABLE OF CONTENTS</h2>
    <ul>
      <li><span>Lorem Ipsum is simply dummy text</span><span>03</span></li>
      <li><span>Lorem Ipsum is simply dummy text</span><span>04</span></li>
      <li><span>Lorem Ipsum is simply dummy text</span><span>05</span></li>
      <li><span>Lorem Ipsum is simply dummy text</span><span>06</span></li>
      <li><span>Lorem Ipsum is simply dummy text</span><span>07</span></li>
    </ul>
  </div>
  <span class="foot-url">www.webaddress.com</span><div class="foot-rule"></div><span class="page-no">02</span>
</div>

<!-- row 2 -->
<div class="slide boxes" style="left:49px;top:1223px">
  <div class="top-rule"></div><span class="brand-mini">Ridgeway DevOps</span>
  <h2 class="heading">HEADING GOES HERE</h2>
  <div class="info-box" style="left:9px;width:171px">
    <h3>HEADING HERE</h3>
    <p>Lorem Ipsum is simply dummy text of the printing and typesetting industry. Lorem Ipsum has been the industry's standard dummy text ever since the 1500s, when an unknown printer took a galley of type and scrambled it to make a type.</p>
    <p>Lorem Ipsum is simply dummy text of the printing and typesetting industry. Lorem Ipsum has been the industry's standard dummy text ever since the 1500s, when an unknown printer took a galley.</p>
  </div>
  <div class="photo" role="img" aria-label="Photo of hands holding a phone over a laptop keyboard" style="left:180px;top:83px;width:182px;height:185px;background:linear-gradient(160deg,#4d3f52,#b79a9a 50%,#d9d4dc)"></div>
  <div class="info-box" style="left:362px;width:165px">
    <h3>HEADING HERE</h3>
    <p>Lorem Ipsum is simply dummy text of the printing and typesetting industry. Lorem Ipsum has been the industry's standard dummy text ever since the 1500s, when an unknown printer took a galley of type and scrambled it to make a type.</p>
    <p>Lorem Ipsum is simply dummy text of the printing and typesetting industry. Lorem Ipsum has been the industry's standard dummy text ever since the 1500s, when an unknown printer took a galley.</p>
  </div>
  <span class="foot-url">www.webaddress.com</span><div class="foot-rule"></div><span class="page-no">03</span>
</div>

<div class="slide title-slide" style="left:632px;top:1223px">
  <div class="top-rule"></div><span class="brand-mini">Ridgeway DevOps</span>
  <div class="center-brand"><span class="dot"></span>Ridgeway DevOps</div>
  <div class="center-title">PRESENTATION TITLE GOES HERE</div>
  <span class="foot-url">www.webaddress.com</span><div class="foot-rule"></div><span class="page-no">04</span>
</div>

<!-- row 3 -->
<div class="slide ring" style="left:49px;top:1576px">
  <div class="top-rule"></div><span class="brand-mini">Ridgeway DevOps</span>
  <h2 class="heading">HEADING GOES HERE</h2>
  <div class="ring-label"><h3>LOREM IPSUM</h3><p>Lorem Ipsum is simply dummy text</p></div>
  <svg class="art" width="541" height="303" viewBox="0 0 541 303">
    <circle cx="259" cy="166" r="78" fill="none" stroke="var(--ink)" stroke-width="3"/>
    <circle cx="259" cy="166" r="70" fill="none" stroke="var(--orange)" stroke-width="10"/>
    <circle cx="259" cy="166" r="60" fill="var(--ink)"/>
    <circle cx="259" cy="166" r="44" fill="none" stroke="#fff" stroke-width="1"/>
    <text x="259" y="166" text-anchor="middle" fill="#fff" font-size="10" font-weight="700" font-family="Source Sans 3, sans-serif">LOREM IPSUM</text>
    <text x="259" y="177" text-anchor="middle" fill="#fff" font-size="6" font-family="Source Sans 3, sans-serif">Lorem Ipsum</text>
    <circle cx="259" cy="90" r="14" fill="var(--ink)" stroke="#fff" stroke-width="2"/>
    <rect x="253" y="88" width="12" height="9" rx="1" fill="#fff"/><path d="M255.5 88v-3a3.5 3.5 0 0 1 7 0v3" fill="none" stroke="#fff" stroke-width="1.5"/>
    <circle cx="259" cy="242" r="14" fill="var(--ink)" stroke="#fff" stroke-width="2"/>
    <rect x="251" y="235" width="16" height="10" rx="1" fill="none" stroke="#fff" stroke-width="1.5"/><path d="M255 249h8" stroke="#fff" stroke-width="1.5"/>
    <g fill="var(--orange)">
      <circle cx="380" cy="104" r="11"/><circle cx="380" cy="148" r="11"/><circle cx="380" cy="196" r="11"/><circle cx="380" cy="243" r="11"/>
    </g>
    <g fill="none" stroke="#fff" stroke-width="1.5" stroke-linecap="round" stroke-linejoin="round">
      <path d="M375 104l4 4 6-8"/>
      <path d="M374 143h12v8h-7l-3 3v-3h-2z"/>
      <path d="M380 202c-4-5-5-7-5-9a5 5 0 0 1 10 0c0 2-1 4-5 9z"/>
      <path d="M374 243h12M382 239l4 4-4 4"/>
    </g>
    <g stroke="var(--arrow)" stroke-width="1"><path d="M337 120l32-12M340 150h28M340 182l29 12M337 212l32 27"/></g>
  </svg>
  <p class="point" style="top:98px">Lorem Ipsum is simply dummy text of<br>the printing.</p>
  <p class="point" style="top:142px">Lorem Ipsum is simply dummy text of<br>the printing.</p>
  <p class="point" style="top:190px">Lorem Ipsum is simply dummy text of<br>the printing.</p>
  <p class="point" style="top:237px">Lorem Ipsum is simply dummy text of<br>the printing.</p>
  <span class="foot-url">www.webaddress.com</span><div class="foot-rule"></div><span class="page-no">05</span>
</div>

<div class="slide grid" style="left:632px;top:1576px">
  <div class="top-rule"></div><span class="brand-mini">Ridgeway DevOps</span>
  <h2 class="heading">HEADING GOES HERE</h2>
  <div class="cell" style="left:14px;top:98px"><i style="background:var(--brown)">A</i><b>Title One</b><span>Lorem Ipsum is simply dummy text of<br>the printing &amp; typesetting industry.</span></div>
  <div class="cell" style="left:14px;top:158px"><i style="background:var(--orange)">B</i><b class="hot">Title Two</b><span>Lorem Ipsum is simply dummy text of<br>the printing &amp; typesetting industry.</span></div>
  <div class="cell" style="left:14px;top:218px"><i style="background:var(--brown)">C</i><b>Title Three</b><span>Lorem Ipsum is simply dummy text of<br>the printing &amp; typesetting industry.</span></div>
  <div class="cell" style="left:199px;top:98px"><i style="background:var(--orange)">D</i><b class="hot">Title Four</b><span>Lorem Ipsum is simply dummy text of<br>the printing &amp; typesetting industry.</span></div>
  <div class="cell" style="left:199px;top:158px"><i style="background:var(--brown)">E</i><b>Title Five</b><span>Lorem Ipsum is simply dummy text of<br>the printing &amp; typesetting industry.</span></div>
  <div class="cell" style="left:199px;top:218px"><i style="background:var(--orange)">F</i><b class="hot">Title Six</b><span>Lorem Ipsum is simply dummy text of<br>the printing &amp; typesetting industry.</span></div>
  <div class="cell" style="left:384px;top:98px"><i style="background:var(--brown)">G</i><b>Title Seven</b><span>Lorem Ipsum is simply dummy text of<br>the printing &amp; typesetting industry.</span></div>
  <div class="cell" style="left:384px;top:158px"><i style="background:var(--orange)">H</i><b class="hot">Title Eight</b><span>Lorem Ipsum is simply dummy text of<br>the printing &amp; typesetting industry.</span></div>
  <div class="cell" style="left:384px;top:218px"><i style="background:var(--brown)">I</i><b>Title Nine</b><span>Lorem Ipsum is simply dummy text of<br>the printing &amp; typesetting industry.</span></div>
  <span class="foot-url">www.webaddress.com</span><div class="foot-rule"></div><span class="page-no">06</span>
</div>

<!-- row 4 -->
<div class="slide steps" style="left:49px;top:1929px">
  <div class="top-rule"></div><span class="brand-mini">Ridgeway DevOps</span>
  <h2 class="heading">HEADING GOES HERE</h2>
  <svg class="art" width="541" height="303" viewBox="0 0 541 303" font-family="Source Sans 3, sans-serif" font-weight="700" font-size="15" fill="#fff" text-anchor="middle">
    <g fill="var(--arrow)"><path d="M107 126h12v-6l11 12-11 12v-6h-12z"/><path d="M248 126h12v-6l11 12-11 12v-6h-12z"/><path d="M389 126h12v-6l11 12-11 12v-6h-12z"/></g>
    <circle cx="60" cy="132" r="33" fill="var(--brown)"/><text x="60" y="137">20%</text>
    <circle cx="201" cy="132" r="33" fill="var(--rust)"/><text x="201" y="137">30%</text>
    <circle cx="342" cy="132" r="33" fill="var(--copper)"/><text x="342" y="137">40%</text>
    <circle cx="476" cy="132" r="33" fill="var(--orange)"/><text x="476" y="137">50%</text>
  </svg>
  <p class="note" style="left:4px;top:176px">Lorem Ipsum is simply dummy text of the printing and typesetting industry.</p>
  <p class="note" style="left:145px;top:176px">Lorem Ipsum is simply dummy text of the printing and typesetting industry.</p>
  <p class="note" style="left:286px;top:176px">Lorem Ipsum is simply dummy text of the printing and typesetting industry.</p>
  <p class="note" style="left:420px;top:176px">Lorem Ipsum is simply dummy text of the printing and typesetting industry.</p>
  <span class="foot-url">www.webaddress.com</span><div class="foot-rule"></div><span class="page-no">07</span>
</div>

<div class="slide curve" style="left:632px;top:1929px">
  <div class="top-rule"></div><span class="brand-mini">Ridgeway DevOps</span>
  <h2 class="heading">HEADING GOES HERE</h2>
  <svg class="art" width="541" height="303" viewBox="0 0 541 303" font-family="Source Sans 3, sans-serif" font-weight="700" fill="#fff" text-anchor="middle">
    <path d="M8 188 C60 180 90 160 122 171 S190 200 224 189 S290 130 328 127 S390 150 423 146 S490 90 520 60" fill="none" stroke="#9a9a9a" stroke-width="1" stroke-dasharray="3 3"/>
    <path d="M512 58l10-4-4 10" fill="none" stroke="#9a9a9a" stroke-width="1"/>
    <g stroke="#777" stroke-width="1"><path d="M122 149v-28"/><path d="M224 165v-60"/><path d="M328 150v26"/><path d="M423 116v-26"/></g>
    <circle cx="122" cy="171" r="22" fill="var(--brown)"/><text x="122" y="175" font-size="11">20%</text>
    <circle cx="224" cy="189" r="24" fill="var(--rust)"/><text x="224" y="193" font-size="12">30%</text>
    <circle cx="328" cy="127" r="24" fill="var(--copper)"/><text x="328" y="131" font-size="12">40%</text>
    <circle cx="423" cy="146" r="30" fill="var(--orange)"/><text x="423" y="151" font-size="14">50%</text>
  </svg>
  <p class="note" style="left:66px;top:232px">Lorem Ipsum is simply dummy text of the printing and typesetting industry.</p>
  <p class="note" style="left:168px;top:72px">Lorem Ipsum is simply dummy text of the printing and typesetting industry.</p>
  <p class="note" style="left:272px;top:178px">Lorem Ipsum is simply dummy text of the printing and typesetting industry.</p>
  <p class="note" style="left:367px;top:58px">Lorem Ipsum is simply dummy text of the printing and typesetting industry.</p>
  <span class="foot-url">www.webaddress.com</span><div class="foot-rule"></div><span class="page-no">08</span>
</div>

<!-- row 5 -->
<div class="slide closing" style="left:49px;top:2280px">
  <div class="closing-brand"><span class="dot"></span>Ridgeway DevOps</div>
  <h2 class="thanks">Thank You!</h2>
  <div class="contact" style="left:312px;top:120px;width:220px">
    <svg width="12" height="12" viewBox="0 0 12 12"><path d="M1 6l5-5 5 5v5H7V8H5v3H1z" fill="#fff"/></svg>
    Address<small>Lorem Ipsum is simply dummy text of the printing &amp; typesetting</small>
  </div>
  <div class="contact" style="left:312px;top:166px">
    <svg width="12" height="12" viewBox="0 0 12 12"><path d="M3 1l2 3-1 1.5c.8 1.6 1.9 2.7 3.5 3.5L9 8l3 2-1.5 2C6 12 0 6 0 2.5z" fill="#fff"/></svg>
    Phone<small>1234 567 8900</small>
  </div>
  <div class="contact" style="left:444px;top:166px">
    <svg width="12" height="12" viewBox="0 0 12 12"><rect x="3" y="1" width="6" height="4" fill="#fff"/><rect x="1" y="5" width="10" height="6" rx="1" fill="#fff"/></svg>
    Fax<small>1234 567 7789</small>
  </div>
  <div class="contact" style="left:312px;top:212px">
    <svg width="12" height="12" viewBox="0 0 12 12"><rect x="1" y="2.5" width="10" height="7" fill="#fff"/><path d="M1 3l5 4 5-4" fill="none" stroke="var(--brown)" stroke-width="1"/></svg>
    E-mail<small>hello@ridgewaydev.co</small>
  </div>
  <div class="contact" style="left:444px;top:212px">
    <svg width="12" height="12" viewBox="0 0 12 12"><circle cx="6" cy="6" r="5" fill="none" stroke="#fff" stroke-width="1.3"/><path d="M1 6h10M6 1c-3 3-3 7 0 10M6 1c3 3 3 7 0 10" fill="none" stroke="#fff" stroke-width="1"/></svg>
    Website<small>www.ridgewaydev.co</small>
  </div>
</div>

<div class="signoff"><span class="dot"></span>Ridgeway DevOps</div>

</body>
</html>
```